Private vineyard wine bottle label design

We need a label for our private vineyard's wine in La Cresta California. The wine will not be for sale, so there are no legal requirements about what can or cannot be on the label. We would like the name of the vineyard "Marcombe Wine Groves" displayed prominently, and to also include
the grape type "Barbera", and optionally the vineyard location. We would like a stylized (but not cartoonish) image of a stoic bull with horns included. I would also like to hide the image of a maple leaf somewhere on the label, it should be subtle and not obvious unless someone is specifically looking for it. We would like a muted color palate, with a light background.

```html
<!DOCTYPE html>
<html lang="en">
<head>
<meta charset="utf-8">
<title>Marcombe Wine Groves – Private Reserve Label</title>
<link rel="stylesheet" href="https://fonts.googleapis.com/css2?family=Bebas+Neue&family=Mrs+Saint+Delafield&family=Marcellus+SC&family=Oswald:wght@600&display=swap">
<style>
  :root {
    --page: #ffffff;
    --label-cream: #d7d3b4;
    --terracotta: #c07460;
    --ink: #3c3a35;
    --art-light: #b9a48c;
    --art-dark: #8a7567;
  }
  * { margin: 0; padding: 0; box-sizing: border-box; }
  html, body {
    width: 1200px;
    height: 1000px;
    overflow: hidden;
    background: var(--page);
  }
  .canvas {
    position: relative;
    width: 1200px;
    height: 1000px;
  }
  .label {
    position: absolute;
    left: 275px;
    top: 52px;
    width: 650px;
    height: 896px;
    background: var(--label-cream);
  }
  .rule {
    position: absolute;
    height: 3px;
    background: var(--terracotta);
  }
  .rule--full { left: 0; width: 100%; }
  .rule--top { top: 77px; }
  .rule--bottom { top: 813px; }
  .rule--inner { left: 98px; width: 453px; }
  .rule--place-top { top: 640px; }
  .rule--place-bottom { top: 714px; }
  .emblem-art {
    position: absolute;
    left: 98px;
    top: 130px;
    width: 453px;
    height: 262px;
    background: linear-gradient(180deg, var(--art-light), var(--art-dark));
  }
  .vineyard-name {
    position: absolute;
    left: 0;
    width: 100%;
    top: 420px;
    text-align: center;
    font-family: "Bebas Neue", "Oswald", sans-serif;
    font-weight: 400;
    font-size: 57px;
    line-height: 1;
    letter-spacing: 0.5px;
    color: var(--terracotta);
  }
  .cuvee {
    position: absolute;
    left: 0;
    width: 100%;
    top: 522px;
    text-align: center;
    font-family: "Mrs Saint Delafield", cursive;
    font-size: 76px;
    line-height: 1;
    color: var(--ink);
  }
  .place {
    position: absolute;
    left: 0;
    width: 100%;
    top: 664px;
    text-align: center;
    font-family: "Marcellus SC", serif;
    font-size: 29px;
    line-height: 1;
    letter-spacing: 3px;
    color: var(--terracotta);
  }
  .volume {
    position: absolute;
    left: 0;
    width: 100%;
    top: 760px;
    text-align: center;
    font-family: "Oswald", sans-serif;
    font-weight: 600;
    font-size: 27px;
    line-height: 1;
    letter-spacing: 1px;
    color: var(--terracotta);
  }
</style>
</head>
<body>
  <main class="canvas">
    <section class="label">
      <div class="rule rule--full rule--top"></div>

      <div class="emblem-art" role="img" aria-label="Illustration of a longhorn bull standing before a large oak tree on a grassy hill"></div>

      <h1 class="vineyard-name">Marcombe Wine Groves</h1>
      <p class="cuvee">Private Reserve</p>

      <div class="rule rule--inner rule--place-top"></div>
      <p class="place">La Cresta - California</p>
      <div class="rule rule--inner rule--place-bottom"></div>

      <p class="volume">Barbera · 750ml</p>

      <div class="rule rule--full rule--bottom"></div>
    </section>
  </main>
</body>
</html>
```